Poster

I need a poster for my business, www.brightharbortastingtours.com which some information about the most important activities (Sangria Tasting, Iberian Ham, Charcuteries & Sherry Wine Tasting, Sailboat Experiences and Picnic Experiences). A3 Format. Social media included (@brightharbortoursbht), contact information included.

```html
<!DOCTYPE html>
<html lang="en">
<head>
<meta charset="utf-8">
<title>Bright Harbor Tasting Tours – Poster</title>
<link href="https://fonts.googleapis.com/css2?family=Montserrat:wght@400;500;600;700&display=swap" rel="stylesheet">
<style>
  :root{
    --stage:#474647;
    --paper:#ffffff;
    --amber:#f2a51f;
    --ink:#111111;
    --muted:#5f5a66;
    --dusk-top:#8f7fa8;
    --dusk-glow:#f0a37a;
    --sea:#4b4257;
  }
  *{box-sizing:border-box;margin:0;padding:0}
  html,body{width:1200px;height:1200px;overflow:hidden;background:var(--stage)}
  body{font-family:"Montserrat",sans-serif;color:var(--ink);position:relative}
  .poster{position:absolute;left:217px;top:62px;width:765px;height:1076px;background:var(--paper);overflow:hidden;box-shadow:0 4px 12px rgba(0,0,0,.35)}
  .hero{position:absolute;left:0;top:0;width:765px;height:480px;
    background:linear-gradient(180deg,var(--dusk-top) 0%,#c98d9c 22%,var(--dusk-glow) 42%,#7b5f72 58%,var(--sea) 72%,#a9a2b4 86%,var(--paper) 100%)}
  .brand{position:absolute;left:19px;top:40px;display:flex;align-items:center;gap:10px}
  .brand-mark{width:22px;height:22px;background:var(--amber)}
  .brand-name{font-weight:700;font-size:22px;line-height:1.1;color:var(--amber);letter-spacing:.5px;text-transform:uppercase}
  .headline{position:absolute;left:0;width:765px;top:300px;text-align:center;color:#fff;font-weight:700;font-size:62px;letter-spacing:-.5px}
  .subline{position:absolute;left:156px;top:380px;width:453px;height:40px;background:var(--amber);color:#fff;font-weight:500;font-size:27px;line-height:40px;text-align:center;white-space:nowrap}
  .intro{position:absolute;left:23px;top:440px;width:719px;font-size:14.6px;line-height:20px;font-weight:500;text-align:justify}
  .section-title{position:absolute;left:219px;top:499px;width:326px;height:42px;text-align:center;font-weight:700;font-size:27px;line-height:42px;
    border-top:1.5px solid var(--amber);border-bottom:1.5px solid var(--amber)}
  .card{position:absolute;width:345px}
  .card h3{font-size:14px;font-weight:700;color:var(--amber);line-height:16px;width:186px}
  .card h3::after{content:"";display:block;width:27px;height:2px;background:var(--amber);margin-top:5px}
  .card p{font-size:12.5px;line-height:19.6px;width:186px;margin-top:6px}
  .card p.duration{margin-top:6px}
  .card b{font-weight:700}
  .photo{position:absolute;left:188px;top:-8px;width:145px;height:124px;border:3px solid var(--amber)}
  .c1{left:23px;top:566px}.c2{left:411px;top:566px}.c3{left:23px;top:772px}.c4{left:411px;top:772px}
  .ph-sangria{background:linear-gradient(135deg,#e9e4df,#9c6a4d 55%,#8c1f25)}
  .ph-ham{background:linear-gradient(135deg,#cfc8bc,#3a332c 55%,#1c4a3c)}
  .ph-sail{background:linear-gradient(180deg,#d9e3ea,#8fb0c7 45%,#2d5f8a)}
  .ph-picnic{background:linear-gradient(135deg,#9fb5c9,#e8e2d8 50%,#8a4b2a)}
  .contact-rule{position:absolute;left:0;top:1001px;width:765px;height:1.5px;background:var(--amber)}
  .contact-title{position:absolute;left:322px;top:986px;padding:0 6px;background:var(--paper);color:var(--amber);font-weight:700;font-size:21px;line-height:30px}
  .pill{position:absolute;top:1032px;height:23px;border-radius:12px;background:var(--amber);display:flex;align-items:center;gap:5px;padding-left:2px;font-size:11px;font-weight:500;white-space:nowrap}
  .pill .icon{width:19px;height:19px;border-radius:50%;background:var(--ink);display:flex;align-items:center;justify-content:center}
  .p1{left:22px;width:250px}.p2{left:302px;width:163px}.p3{left:492px;width:250px}
</style>
</head>
<body>
<main class="poster">
  <div class="hero" role="img" aria-label="Sunset over the sea on the Marbella coast with palm trees on a headland"></div>

  <div class="brand">
    <span class="brand-mark"></span>
    <span class="brand-name">Bright Harbor<br>Tasting Tours</span>
  </div>

  <h1 class="headline">Enjoy Marbella</h1>
  <div class="subline">with Bright Harbor Tasting Tours</div>

  <p class="intro">Dive into a world of culinary delights set against a backdrop of awe-inspiring beauty. Join us and treat yourself to the best of Marbella’s flavors with a side of stunning scenery.</p>

  <h2 class="section-title">Try Our Experiences</h2>

  <section class="card c1">
    <h3>Sangria Tasting</h3>
    <p><b>Inclusions:</b> Sampling of 4 types unique and delightful variations of classic Spanish Sangria: Sherry Wine Sangria, White Wine Sangria, Red Wine Sangria and Rose Cava Sangria.</p>
    <p class="duration"><b>Duration:</b> 1hr and 30min.</p>
    <div class="photo ph-sangria" role="img" aria-label="Friends enjoying glasses of sangria at an outdoor table"></div>
  </section>

  <section class="card c2">
    <h3>Iberian Ham, Charcuteries &amp; Sherry Wine Tasting</h3>
    <p><b>Inclusions:</b> Sample two premium Iberian hams, three distinct sausages, and a variety of olives, all perfectly paired with a selection of Sherry wines.</p>
    <p class="duration"><b>Duration:</b> 1hr and 30min.</p>
    <div class="photo ph-ham" role="img" aria-label="Glass of olives and small tapas on a green board"></div>
  </section>

  <section class="card c3">
    <h3>Sailboat Experience</h3>
    <p><b>Inclusions:</b> A tasting of artisanal sangrias and premium wines. Gourmet appetizers including cheese, iberian saussage, and olives. Stunning panoramic views of the Estepona coast.</p>
    <p class="duration"><b>Duration:</b> 2hr.</p>
    <div class="photo ph-sail" role="img" aria-label="Sailboat cruising on a calm blue sea"></div>
  </section>

  <section class="card c4">
    <h3>Picnic Experience</h3>
    <p><b>Inclusions:</b> Choice of gourmet picnic basket filled with artisanal cheeses, freshly baked bread, cured meats, olives, seasonal fruits, and decadent desserts. Bottle of premium Spanish wine or refreshing beverages.</p>
    <p class="duration"><b>Duration:</b> 2hr.</p>
    <div class="photo ph-picnic" role="img" aria-label="Picnic basket with bread, wine and pastries by the sea"></div>
  </section>

  <div class="contact-rule"></div>
  <h2 class="contact-title">Contact Us</h2>

  <div class="pill p1">
    <span class="icon"><svg width="13" height="13" viewBox="0 0 14 14" fill="none" stroke="#fff" stroke-width="1.1"><circle cx="7" cy="7" r="6"/><ellipse cx="7" cy="7" rx="2.6" ry="6"/><line x1="1" y1="7" x2="13" y2="7"/><line x1="2" y1="4" x2="12" y2="4"/><line x1="2" y1="10" x2="12" y2="10"/></svg></span>
    www.brightharbortastingtours.com
  </div>
  <div class="pill p2">
    <span class="icon"></span>
    @brightharbortoursbht
  </div>
  <div class="pill p3">
    <span class="icon"><svg width="12" height="10" viewBox="0 0 12 10" fill="none" stroke="#fff" stroke-width="1.1"><rect x="0.6" y="0.6" width="10.8" height="8.8" rx="1"/><polyline points="0.8,1 6,5.6 11.2,1"/></svg></span>
    info@brightharbortastingtours.com
  </div>
</main>
</body>
</html>
```